Freelancer Information Security professional needs a business card

I need a simple, young, elegant business card. I'm a freelancer in the InfoSec area and want to be able to give my card to potential customers and new people I meet.

I'd like to have a clean, professional look but at same time not boring or corporate.

The only requirement is to have my "introduction" phrase which is:
"Half hacker, half mercenary."

I have added a card I have as a example, which I think it gives a good example of style I want.

Target Market(s)

Technology / Computers / Engineering

Industry/Entity Type

Information Technology

Contact Information for Business Card

Contact fields I want included:

(351) 93 708 12 54
tomas@vornel.im
https://vornel.im

Font styles to use
Sans Serif

Requirements
Nice to have
• Card doesn't need to have a doubled side, but it looks good / fits the design then please do include.
Should not have
• Outdated graphics or images; too much patterns/colors.

```html
<!DOCTYPE html>
<html lang="en">
<head>
<meta charset="utf-8">
<title>Tomas Vornel – Business Card</title>
<link rel="stylesheet" href="https://fonts.googleapis.com/css2?family=Montserrat:wght@600;700&family=Questrial&display=swap">
<style>
  :root {
    --backdrop: #e9e7e5;
    --card: #ffffff;
    --crimson: #8e0911;
    --crimson-light: #b3141d;
    --crimson-dark: #7a050c;
    --ink: #141414;
    --paper-white: #ffffff;
  }
  * { box-sizing: border-box; margin: 0; padding: 0; }
  html, body {
    width: 1200px;
    height: 960px;
    overflow: hidden;
    background: var(--backdrop);
  }
  .stage {
    width: 1200px;
    height: 960px;
    display: flex;
    align-items: center;
    justify-content: center;
  }
  .card {
    position: relative;
    width: 900px;
    height: 514px;
    background: var(--card);
    box-shadow: 0 18px 40px rgba(0, 0, 0, 0.18), 0 2px 6px rgba(0, 0, 0, 0.08);
    text-align: center;
  }
  .identity {
    position: absolute;
    top: 88px;
    left: 0;
    right: 0;
  }
  .identity__name {
    font-family: "Montserrat", sans-serif;
    font-weight: 700;
    font-size: 46px;
    letter-spacing: -0.5px;
    line-height: 1;
    color: var(--crimson);
  }
  .identity__role {
    margin-top: 6px;
    padding-left: 70px;
    font-family: "Montserrat", sans-serif;
    font-weight: 600;
    font-size: 18px;
    color: var(--ink);
  }
  .motto-band {
    position: absolute;
    top: 214px;
    left: 0;
    right: 0;
    height: 104px;
    display: flex;
    align-items: center;
    justify-content: center;
    background: linear-gradient(90deg, var(--crimson-dark) 0%, var(--crimson) 35%, var(--crimson-light) 70%, var(--crimson-dark) 100%);
  }
  .motto-band__quote {
    font-family: "Questrial", sans-serif;
    font-size: 54px;
    letter-spacing: 0.5px;
    color: var(--paper-white);
  }
  .contact {
    position: absolute;
    top: 348px;
    left: 0;
    right: 0;
    list-style: none;
    font-family: "Questrial", sans-serif;
    font-size: 23px;
    line-height: 1.38;
    color: var(--ink);
  }
</style>
</head>
<body>
  <main class="stage">
    <article class="card">
      <header class="identity">
        <h1 class="identity__name">Tomas Vornel</h1>
        <p class="identity__role">Chief Creative Officer</p>
      </header>
      <div class="motto-band">
        <p class="motto-band__quote">"Half hacker, half mercenary."</p>
      </div>
      <ul class="contact">
        <li class="contact__phone">(351) 93 708 12 54</li>
        <li class="contact__email">tomas@vornel.im</li>
        <li class="contact__web">https://vornel.im</li>
      </ul>
    </article>
  </main>
</body>
</html>
```